Anzeigengestaltung für einen einen ambulanten Pflegedienst
Zielgruppe
Insgesamt möchte ich gern drei Anzeigen für das Internet gestalten haben. Ich betreibe einen ambulanten Pflegedienst. Die erste Anzeige soll dazu dienen Kunden anzusprechen, die einen Unterstützungsbedarf und / oder einen Beratungsbedarf haben. Die zweite Anzeige soll dazu dienen neues Personal anzuwerben. Die dritte Anzeige soll speziell potenzielle Azubis ansprechen. Die Anzeigen sind gedacht für Chatterwall und Pixelora hauptsächlich. In den Druck sollte es schon 10cm x 8cm sein. Es wäre super wenn vielleicht auch eine Art Aufruf an ehrenamtliche Mitarbeiter erfolgt.
Aufgabenstellung
Die Anzeigen sollen den Stil der Homepage beibehalten. Freundlich, frisch und agil wirken. Alle sollten emotional ansprechend sein und gerade der für zukünftige Mitarbeiter sollte deutlich ein gutes Betriebsklima vermitteln. Als Datei habe ich einige Bilder, die bereits für die Homepage oder Flyer verwendet wurden hochgeladen. des Weiteren habe ich die einzelnen Seiten des Flyers hochgeladen.

```html
<!DOCTYPE html>
<html lang="de">
<head>
<meta charset="utf-8">
<title>Elmaro Pflege – Karriere</title>
<link rel="stylesheet" href="https://fonts.googleapis.com/css2?family=Playfair+Display:wght@400&family=Quicksand:wght@500;700&display=swap">
<style>
  :root {
    --teal: #4aafad;
    --green: #7bb03c;
    --grey: #646464;
    --white: #ffffff;
    --ring: #eeeee6;
    --photo-teal: #3f8e8a;
    --photo-skin: #c99d88;
    --photo-light: #e4dfe7;
  }
  * { margin: 0; padding: 0; box-sizing: border-box; }
  html, body { width: 1200px; height: 960px; overflow: hidden; background: var(--white); }
  .ad {
    position: relative;
    width: 1200px;
    height: 960px;
    overflow: hidden;
    background: var(--white);
    font-family: "Quicksand", sans-serif;
  }
  .photo {
    position: absolute;
    left: 630px;
    top: -80px;
    width: 1120px;
    height: 1120px;
    border-radius: 50%;
    background: linear-gradient(160deg, #b9bec4 0%, var(--photo-light) 22%, var(--photo-skin) 45%, var(--photo-teal) 62%, var(--photo-skin) 78%, var(--photo-light) 100%);
  }
  .tagline {
    position: absolute;
    left: 60px;
    top: 60px;
    font-family: "Playfair Display", serif;
    font-size: 37px;
    color: var(--grey);
    font-weight: 400;
  }
  .headline {
    position: absolute;
    left: 58px;
    top: 118px;
    font-weight: 700;
    font-size: 66px;
    line-height: 76px;
  }
  .headline .line-teal { color: var(--teal); display: block; }
  .headline .line-green { color: var(--green); display: block; }
  .rule {
    position: absolute;
    left: 60px;
    top: 288px;
    width: 454px;
    height: 5px;
    background: var(--green);
  }
  .requirements {
    position: absolute;
    left: 60px;
    top: 366px;
    list-style: none;
  }
  .requirements li {
    font-size: 41px;
    font-weight: 500;
    color: var(--grey);
    height: 76px;
    line-height: 56px;
    white-space: nowrap;
  }
  .requirements li::before {
    content: "+";
    color: var(--green);
    font-weight: 700;
    display: inline-block;
    width: 37px;
  }
  .cta {
    position: absolute;
    left: 45px;
    top: 838px;
    width: 587px;
    height: 62px;
    border-radius: 31px;
    background: var(--teal);
    color: var(--white);
    font-family: "Playfair Display", serif;
    font-size: 33px;
    line-height: 62px;
    padding-left: 27px;
    white-space: nowrap;
  }
  .brand-badge {
    position: absolute;
    left: 655px;
    top: 44px;
    width: 242px;
    height: 242px;
    border-radius: 50%;
    background: var(--white);
    border: 4px solid var(--ring);
    display: flex;
    flex-direction: column;
    align-items: center;
    justify-content: center;
    gap: 18px;
  }
  .brand-dot {
    width: 56px;
    height: 56px;
    border-radius: 50%;
    background: var(--teal);
  }
  .brand-name {
    font-family: "Quicksand", sans-serif;
    font-weight: 700;
    font-size: 25px;
    color: var(--grey);
    letter-spacing: 0.5px;
  }
</style>
</head>
<body>
<main class="ad">
  <div class="photo" role="img" aria-label="Foto: Pflegekraft in türkisfarbener Kleidung hört mit einem Stethoskop den Oberkörper eines Patienten ab"></div>

  <p class="tagline">Pflege mit Herz &amp; Seele</p>
  <h1 class="headline">
    <span class="line-teal">Komm in unser</span>
    <span class="line-green">Team Pflege</span>
  </h1>
  <div class="rule"></div>

  <ul class="requirements">
    <li>Teamfähigkeit</li>
    <li>Hilfsbereitschaft</li>
    <li>Engagement</li>
    <li>Führerschein Klasse B</li>
    <li>Gute Deutschkenntnisse</li>
  </ul>

  <div class="cta">www.elmaro-pflege.de/karriere/</div>

  <div class="brand-badge">
    <span class="brand-dot"></span>
    <span class="brand-name">ELMARO PFLEGE</span>
  </div>
</main>
</body>
</html>
```